A 1 to 2 page digital flyer, using my existing logo and branding files.

I need a professional1 to 2 page flyer in both digital file and an editable PDF form to advertise service offerings for my coaching and consulting business.
The flyer should be upmarket, professional and conservative in style to meet the expectations of my professional market (doctors, psychologists and executives).
It will be based on my existing logo and brand, see my current website: www.marlowadvisory.net
Here are the key elements needed:
1) First the main product offering (which I should be able to edit myself for future use). In this first case, this features an advertisement for a 'Therapy group for professionals'. (see attached file).
2) The second key text is my bio/profile which includes a photo.
3) The third section is a call to action, including my contact details.
4) The flyer should include my email, website and phone contact details.
5) It should also include some small logos of my professional accrediting organisations.

Target Market(s)

Doctors, psychologists, executives in healthcare.

Industry/Entity Type

Health care and business schools

Font styles to use
Other font styles liked:
• Operetta (headings), Sofia Pro (body text).

Colors
0054AA
0677BA
7BADD7
CADEEF
E8F1F8

Requirements
Must have
• 1. Strong adherence to my brand voice and design elements, as featured on my website and in my branded stationery. 2. Editable text sections in PDF that I can re-use for future advertisements. 3. Suitable size and medium (e.g. A4 size) for sharing digitally via my website, email, and social media. 4) Very prompt design as soon as possible please - quick turnaround will secure the winning place.
Nice to have
• Please use design images and inspiration from my website. An additional stock photo of a therapy group is uploaded as an example
Should not have
• Do not deviate from my brand voice, fonts and colours please.

```html
<!DOCTYPE html>
<html lang="en">
<head>
<meta charset="utf-8">
<title>Marlow Advisory – Therapy Group Flyer</title>
<link rel="stylesheet" href="https://fonts.googleapis.com/css2?family=Playfair+Display:wght@400;500&family=Mulish:ital,wght@0,400;0,600;0,700;1,600;1,700&display=swap">
<style>
  :root{
    --brand-deep:#0054AA;
    --brand-mid:#3A6DB9;
    --brand-light:#7BADD7;
    --brand-pale:#CADEEF;
    --brand-mist:#E8F1F8;
    --ink:#2b2b2b;
    --canvas:#000;
    --paper:#fff;
    --footer-grey:#eef0f3;
  }
  *{box-sizing:border-box;margin:0;padding:0}
  html,body{width:1200px;height:1200px;overflow:hidden;background:var(--canvas)}
  body{position:relative;font-family:"Mulish",sans-serif;color:var(--ink)}
  h1,h2{font-weight:400}
  .page{position:absolute;background:var(--paper);overflow:hidden;width:547px;height:776px}
  .page--offer{left:37px;top:60px}
  .page--profile{left:607px;top:354px}
  .abs{position:absolute}
  .brand-name{font-family:"Playfair Display",serif;color:var(--brand-deep);font-weight:400;line-height:1.05}
  .brand-mark{background:var(--brand-deep)}

  /* offer page */
  .offer-hero{left:0;top:0}
  .offer-brand{left:16px;top:30px;display:flex;align-items:center;gap:14px}
  .offer-brand .brand-mark{width:40px;height:40px}
  .offer-brand .brand-name{font-size:27px}
  .offer-title{left:0;right:0;top:176px;text-align:center;font-family:"Playfair Display",serif;font-size:28px;color:var(--brand-deep);font-weight:400}
  .offer-body{left:24px;right:24px;top:228px;text-align:center;font-size:10.4px;line-height:1.32}
  .offer-body p{margin-bottom:11px}
  .quote{font-style:italic;font-weight:700;color:#111}
  .quote-name{display:block;font-style:normal;color:var(--brand-deep);font-weight:700}
  .offer-band{left:0;top:536px;width:547px;height:178px;background:var(--brand-mid);color:#fff;text-align:center;font-size:10.4px;line-height:1.32;padding:18px 24px 0}
  .offer-band p{margin-bottom:10px}
  .offer-footer{left:0;top:714px;width:547px;height:62px;background:var(--footer-grey);text-align:center;font-size:10.4px;line-height:1.3;padding-top:10px}
  .offer-footer strong{font-style:italic;font-size:12.5px;display:block;color:#111}

  /* profile page */
  .profile-accent{left:0;top:0}
  .profile-brand{right:18px;top:18px;display:flex;align-items:center;gap:6px}
  .profile-brand .brand-mark{width:13px;height:13px}
  .profile-brand .brand-name{font-size:11px}
  .profile-photo{left:34px;top:72px;width:175px;height:268px}
  .profile-name{left:239px;top:66px;font-family:"Playfair Display",serif;font-size:29px;font-weight:400;color:var(--brand-deep)}
  .profile-role{left:239px;top:104px;font-size:10px;font-weight:700;color:var(--brand-deep)}
  .profile-bio{left:239px;top:128px;width:273px;font-size:10.2px;line-height:1.28;text-align:justify;color:#333}
  .profile-bio p{margin-bottom:11px}
  .affiliations{left:240px;top:410px;display:flex;gap:12px}
  .affiliation{width:42px;height:42px;background:var(--brand-deep)}
  .affiliation:nth-child(2){background:#b51f2e}
  .affiliation:nth-child(4){background:#fff;border:1px solid var(--brand-pale)}
  .affiliation:nth-child(5){background:#fff;border:1px solid var(--brand-pale)}
  .cta-band{left:0;top:482px;width:547px;height:53px;background:var(--brand-mid);color:#fff;font-family:"Playfair Display",serif;font-size:24px;padding:12px 0 0 26px}
  .cta-sub{left:0;top:535px;width:547px;height:47px;background:var(--brand-pale);color:var(--brand-deep);font-weight:700;font-size:13px;padding:14px 0 0 26px}
  .contact-area{left:0;top:582px;width:547px;height:194px;background:linear-gradient(90deg,#f7f8fa,#eceef1)}
  .contact-deco{right:0;top:0}
  .contact-name{left:64px;top:18px;font-family:"Playfair Display",serif;font-size:23px;color:var(--brand-deep)}
  .contact-list{left:42px;top:57px;font-size:10.5px;line-height:1.3;color:#333}
  .contact-row{display:flex;align-items:flex-start;gap:10px;margin-bottom:4px}
  .contact-row svg{flex:none;margin-top:1px}
  .contact-row b{color:#111}
  .contact-web{font-weight:700;color:var(--brand-deep);font-size:12.5px}
  .accredit{left:384px;top:98px;width:150px;text-align:center;font-size:10px;color:#333}
  .accredit-badges{display:flex;gap:10px;justify-content:center;margin-top:8px;align-items:center}
  .badge{width:24px;height:24px;border-radius:50%;background:var(--brand-light)}
  .badge--wide{width:38px;height:18px;border-radius:2px;background:var(--brand-deep)}
</style>
</head>
<body>

<section class="page page--offer">
  <svg class="abs offer-hero" width="547" height="230" viewBox="0 0 547 230" role="img" aria-label="Photograph of water droplet ripples on a pale surface">
    <defs>
      <linearGradient id="ripple" x1="0" y1="1" x2="1" y2="0">
        <stop offset="0" stop-color="#f2f4f7"/>
        <stop offset="0.6" stop-color="#dde2e9"/>
        <stop offset="1" stop-color="#c9d0da"/>
      </linearGradient>
    </defs>
    <polygon points="0,170 0,210 547,60 547,0 190,0" fill="url(#ripple)"/>
  </svg>
  <div class="abs offer-brand">
    <div class="brand-mark"></div>
    <div class="brand-name">Marlow<br>Advisory</div>
  </div>
  <h1 class="abs offer-title">A Therapy Group for Professional</h1>
  <div class="abs offer-body">
    <p>This is a new, online analytic group for professionals seeking to engage<br>more authentically with their personal and professional selves.</p>
    <p class="quote">“You bare your heart and share things that you wouldn’t under normal circumstances.<br>You get to know each other very well, very quickly. There’s that sort of intense,<br>shared experience that comes from speaking to each other’s lives.”<span class="quote-name">(Helen, medical director)</span></p>
    <p>Designed for professionals who work in health and other human service organisations,<br>this group focuses on the emotional needs of staff who work in emotionally demanding settings.</p>
    <p>Working in these caring professions often present immense challenges that, over time,<br>affect both personal and professional lives.</p>
    <p>This unique therapy group for professionals creates a confidential environment<br>for a group of peers to explore and develop meaningful change in their lives.</p>
    <p class="quote">“This was really powerful because you feel able to tell the truth to yourself.<br>I needed to deal with this because you keep quiet about things you regret…<br>I could finally open up and clean up my act. So this has changed me”<span class="quote-name">(Peter, school principal)</span></p>
  </div>
  <div class="abs offer-band">
    <p>Aimed at a diverse range of staff and levels of seniority across health, social care,<br>education, and related settings, the group is intended for post-qualification professionals.</p>
    <p>Held online on Thursday evenings (AEST) via Meetlink, it is open to people<br>across Australia and internationally.</p>
    <p>The group is conducted independently and will operate sliding-scale group membership fees.<br>It is not intended for Healthcover or other health insurance cover.</p>
    <p>New members may join and leave the group once they feel the time is right,<br>usually ranging from around six months to potentially several years.</p>
  </div>
  <div class="abs offer-footer">
    <strong>If you are ready to create meaningful change,</strong>
    or for further information, please email or call Prof Daniel Marlow<br>to arrange a confidential conversation.
  </div>
</section>

<section class="page page--profile">
  <svg class="abs profile-accent" width="547" height="480" viewBox="0 0 547 480" aria-hidden="true">
    <polygon points="0,20 95,70 0,150" fill="var(--brand-mid)"/>
    <polygon points="209,150 300,110 300,240 209,280" fill="var(--brand-mist)"/>
  </svg>
  <div class="abs profile-brand">
    <div class="brand-mark"></div>
    <div class="brand-name">Marlow<br>Advisory</div>
  </div>
  <div class="abs profile-photo" role="img" aria-label="Portrait photograph of Professor Daniel Marlow outdoors in a navy suit" style="background:linear-gradient(160deg,#8fa776 0%,#5f7a52 45%,#2c3c5c 100%)"></div>
  <h2 class="abs profile-name">Daniel Marlow</h2>
  <div class="abs profile-role">Professor of Organisational Culture and Leadership</div>
  <div class="abs profile-bio">
    <p>Daniel is a specialist in the deep personal change that professionals need in their lives and work. He works with professionals and leaders across private, public and government organisations, helping them catalyse personal and cultural change.</p>
    <p>In his work as a professor at Halvernmoor University, Thornwick College and Eastvale University, he has developed specialist expertise in creating cultural change, particularly in healthcare. He is an accredited psychoanalytic psychotherapist, group analyst and certified executive coach.</p>
    <p>Before his business-school career, he was a public health service clinical director and lead consultant psychotherapist. He worked in major teaching hospitals in Manchester, Liverpool and London. He holds a PhD in organisational culture and leadership from the Calloway Institute.</p>
  </div>
  <div class="abs affiliations" aria-label="Affiliated institutions">
    <div class="affiliation"></div><div class="affiliation"></div><div class="affiliation"></div><div class="affiliation"></div><div class="affiliation"></div>
  </div>
  <div class="abs cta-band">Are you ready to create meaningful change?</div>
  <div class="abs cta-sub">Book a confidential conversation with Prof Daniel Marlow</div>
  <div class="abs contact-area">
    <svg class="abs contact-deco" width="200" height="194" viewBox="0 0 200 194" role="img" aria-label="Soft white geometric shapes">
      <polygon points="20,194 20,40 60,0 200,0 200,194" fill="#f9fafb"/>
      <polygon points="20,40 60,0 60,194 20,194" fill="#e4e7eb"/>
    </svg>
    <div class="abs contact-name">Professor Daniel Marlow</div>
    <div class="abs contact-list">
      <div class="contact-row">
        <svg width="11" height="11" viewBox="0 0 24 24"><path d="M6.6 10.8a15 15 0 006.6 6.6l2.2-2.2c.3-.3.7-.4 1-.2 1.1.4 2.3.6 3.6.6.6 0 1 .4 1 1V20c0 .6-.4 1-1 1A17 17 0 013 4c0-.6.4-1 1-1h3.5c.6 0 1 .4 1 1 0 1.3.2 2.5.6 3.6.1.3 0 .7-.2 1z" fill="var(--brand-deep)"/></svg>
        <span>+61 3 9012 5530</span>
      </div>
      <div class="contact-row">
        <svg width="11" height="11" viewBox="0 0 24 24"><rect x="2" y="5" width="20" height="14" fill="none" stroke="var(--brand-deep)" stroke-width="2"/><path d="M2 6l10 7 10-7" fill="none" stroke="var(--brand-deep)" stroke-width="2"/></svg>
        <span>info@marlowadvisory.net</span>
      </div>
      <div class="contact-row" style="margin-top:10px">
        <svg width="11" height="13" viewBox="0 0 24 28"><path d="M12 0a9 9 0 00-9 9c0 7 9 19 9 19s9-12 9-19a9 9 0 00-9-9zm0 12a3 3 0 110-6 3 3 0 010 6z" fill="var(--brand-deep)"/></svg>
        <span><b>Address</b><br>Suite 12/48 Elgin Lane<br>Fitzroy, Victoria, Australia</span>
      </div>
      <div class="contact-row" style="margin-top:12px">
        <svg width="11" height="11" viewBox="0 0 24 24"><circle cx="12" cy="12" r="10" fill="none" stroke="var(--brand-deep)" stroke-width="2"/><path d="M2 12h20M12 2c3 3 3 17 0 20M12 2c-3 3-3 17 0 20" fill="none" stroke="var(--brand-deep)" stroke-width="2"/></svg>
        <span class="contact-web">marlowadvisory.net</span>
      </div>
    </div>
    <div class="abs accredit">
      Accredited by:
      <div class="accredit-badges"><div class="badge"></div><div class="badge--wide badge"></div><div class="badge" style="background:#7b5cb0"></div></div>
    </div>
  </div>
</section>

</body>
</html>
```